Mental Health care Company in Washington DC

We are a new mental health care services provider in Washington DC. Please look at these sites.
https://quarrystonewellbeingpartners.com
https://www.quietharborllc.com
https://fernvale-nb.org/
https://www.truepathnb.com
https://www.willowmeadnb.com

```html
<!DOCTYPE html>
<html lang="en">
<head>
<meta charset="utf-8">
<title>Tovan Health Services</title>
<link href="https://fonts.googleapis.com/css2?family=Poppins:ital,wght@0,400;0,500;0,600;0,700;1,400&display=swap" rel="stylesheet">
<style>
:root{
  --navy:#0e1d3f;
  --orange:#f47f20;
  --teal:#a5dadd;
  --teal-soft:#eef8f8;
  --text:#4a5160;
  --white:#ffffff;
}
*{box-sizing:border-box;margin:0;padding:0}
html,body{width:1200px;height:3822px;overflow:hidden}
body{font-family:"Poppins",sans-serif;color:var(--navy);background:var(--white);position:relative}
section,header,footer{position:absolute;left:0;width:1200px}
.abs{position:absolute}
.photo{position:absolute}
.btn{position:absolute;display:flex;align-items:center;justify-content:center;border-radius:22px;font-size:15px;font-weight:500;text-transform:uppercase;letter-spacing:.3px}
.btn-orange{background:var(--orange);color:var(--white)}
.btn-teal{background:var(--teal);color:var(--navy)}
p{color:var(--text)}

/* header */
.site-header{top:0;height:92px;border-bottom:2px solid #eef6f6}
.brand{left:60px;top:20px}
.brand-name{font-size:36px;font-weight:500;color:var(--navy);line-height:1}
.brand-sub{font-size:12px;letter-spacing:7px;color:#8a96a6;margin-top:4px;padding-left:34px}
.nav{right:60px;top:36px;display:flex;gap:33px;font-size:14px}
.nav a{color:var(--navy);text-decoration:none}
.nav a.active{color:var(--orange)}

/* hero */
.hero{top:92px;height:583px}
.hero h1{left:60px;top:100px;font-size:48px;font-weight:700;line-height:1.15}
.hero .lead{left:60px;top:228px;width:430px;font-size:14px;line-height:23px}
.stat{top:380px}
.stat b{display:block;font-size:31px;font-weight:600;color:var(--navy)}
.stat hr{width:42px;border:0;border-top:2px solid #cfe9ea;margin:6px 0 10px}
.stat span{font-size:15px;color:var(--text);line-height:19px;display:block}
.hero-frame-top{left:641px;top:59px;width:410px;height:430px;border-left:6px solid var(--teal);border-top:6px solid var(--teal);border-radius:32px 0 0 0}
.hero-frame-bot{left:700px;top:130px;width:410px;height:398px;border-right:8px solid var(--orange);border-bottom:8px solid var(--orange);border-radius:0 0 32px 0}
.hero-photo{left:650px;top:68px;width:450px;height:451px;border-radius:0 0 28px 28px;background:linear-gradient(135deg,#c9b49a,#e9e1d4 45%,#4fb6b6 80%,#d9d3cc)}

/* services */
.services{top:675px;height:571px;background:var(--teal-soft)}
.section-title{width:100%;text-align:center;font-size:35px;font-weight:500}
.services .section-title{top:70px}
.card{top:151px;width:349px;height:344px;background:var(--white);border-radius:18px;overflow:hidden}
.card .photo{left:0;top:0;width:349px;height:172px;border-radius:18px 18px 18px 18px}
.card h3{position:absolute;left:22px;top:194px;font-size:19px;font-weight:500}
.card p{position:absolute;left:22px;top:230px;width:300px;font-size:13px;line-height:22px}
.card .btn{left:20px;top:288px;width:135px;height:36px}

/* about */
.about{top:1246px;height:611px}
.about h2{left:60px;top:130px;font-size:35px;font-weight:500;line-height:41px}
.about h4{position:absolute;left:60px;font-size:19px;font-weight:400;color:var(--orange)}
.about p{position:absolute;left:60px;font-size:13px;line-height:20px}
.about-big{left:741px;top:74px;width:358px;height:412px;border-radius:0 80px 0 0;background:linear-gradient(160deg,#f1ece2,#d9c39a 40%,#c87a52 65%,#9aa56c)}
.about-small{left:638px;top:326px;width:176px;height:209px;border-radius:0 0 50px 0;background:linear-gradient(160deg,#6fb8ae,#3e4a3c 55%,#c8a86c)}

/* testimonials */
.testimonials{top:1857px;height:490px;background:var(--teal-soft)}
.testimonials h2{left:0;top:68px;width:100%;text-align:center;font-size:35px;font-weight:500;line-height:41px}
.stars{left:0;top:180px;width:100%;display:flex;justify-content:center;gap:8px}
.quote{left:430px;top:216px;width:340px;text-align:center;font-style:italic;font-size:15.5px;line-height:24px}
.client{left:549px;top:330px;display:flex;align-items:center;gap:14px;font-size:13px;color:var(--text)}
.avatar{width:52px;height:52px;border-radius:50%;background:linear-gradient(135deg,#5a6470,#c9a58a)}
.t-photo{border-radius:0 0 0 0}

/* who we are */
.who{top:2347px;height:582px}
.who-frame-top{left:178px;top:78px;width:322px;height:400px;border-left:6px solid var(--orange);border-top:6px solid var(--orange);border-radius:42px 0 0 0}
.who-frame-bot{left:225px;top:120px;width:322px;height:383px;border-right:5px solid var(--teal);border-bottom:5px solid var(--teal)}
.who-photo{left:185px;top:85px;width:355px;height:412px;background:linear-gradient(135deg,#d8dee0,#e8c9ae 45%,#3f8ec4 75%,#e0e4e7)}
.who h2{left:614px;top:172px;font-size:33px;font-weight:500}
.who p{position:absolute;left:614px;top:232px;width:420px;font-size:13.5px;line-height:23px}
.who .btn{left:611px;top:367px;width:142px;height:36px}

/* appointment */
.booking{top:2929px;height:546px;background:linear-gradient(180deg,#f5fbfb,#ffffff 60%)}
.booking .section-title{top:70px}
.field{position:absolute;left:262px;width:675px;height:44px;border:1px solid #f3cfb6;border-radius:24px;font-size:13px;color:var(--navy);padding:14px 0 0 30px}
.field.filled{background:#fdeee5;border-color:#fdeee5}
.field.notes{height:98px;border-radius:30px}
.booking .btn{left:532px;top:434px;width:134px;height:36px}

/* footer */
.site-footer{top:3475px;height:347px;background:var(--teal)}
.site-footer h5{position:absolute;top:45px;font-size:17px;font-weight:500;color:var(--navy)}
.contact-row{position:absolute;left:60px;display:flex;align-items:center;gap:12px;font-size:13.5px;line-height:19px;color:var(--navy)}
.icon-ring{width:34px;height:34px;border-radius:50%;border:2px solid var(--navy);display:flex;align-items:center;justify-content:center;flex:none}
.hours{position:absolute;left:426px;top:90px;font-size:13.5px;line-height:24px;color:var(--navy)}
.hours b{font-weight:600;display:inline-block;width:40px}
.news p{position:absolute;left:791px;top:82px;width:270px;font-size:13px;line-height:20px;color:var(--navy)}
.news .field{left:791px;top:138px;width:348px;height:38px;border-color:var(--navy);padding:10px 0 0 22px;font-size:13px}
.site-footer .btn{left:791px;top:197px;width:134px;height:36px}
.copy-line{left:60px;top:295px;width:1080px;border-top:1px solid #7fbfc2}
.copy{left:0;top:313px;width:100%;text-align:center;font-size:13px;color:var(--navy)}
</style>
</head>
<body>

<header class="site-header">
  <div class="abs brand">
    <div class="brand-name">Tovan Health</div>
    <div class="brand-sub">SERVICES</div>
  </div>
  <nav class="abs nav">
    <a class="active" href="#">Home</a><a href="#">Services</a><a href="#">About</a><a href="#">Testimonial</a><a href="#">Appointment</a><a href="#">Contact</a>
  </nav>
</header>

<section class="hero">
  <h1 class="abs">Tovan Health<br>Services</h1>
  <p class="abs lead">Lorem Ipsum is simply dummy text of the printing and typesetting industry. Sed ut perspiciatis unde omnis iste natus error sit voluptatem lorem ipsum dolor</p>
  <div class="btn btn-orange" style="left:60px;top:307px;width:150px;height:41px">Appointment</div>
  <div class="btn btn-teal" style="left:215px;top:307px;width:150px;height:41px">Contact</div>
  <div class="abs stat" style="left:60px"><b>20+</b><hr><span>Years of<br>experience</span></div>
  <div class="abs stat" style="left:196px"><b>840+</b><hr><span>Patients received<br>help this year</span></div>
  <div class="abs stat" style="left:373px"><b>98%</b><hr><span>Client improved<br>their condition</span></div>
  <div class="abs hero-frame-top"></div>
  <div class="abs hero-frame-bot"></div>
  <div class="photo hero-photo" role="img" aria-label="Nurse in teal scrubs talking with an older woman holding a tablet on a sofa"></div>
</section>

<section class="services">
  <h2 class="abs section-title">Tovan Health Services</h2>
  <article class="abs card" style="left:60px">
    <div class="photo" role="img" aria-label="Trainer helping a man exercise on a ball in a gym" style="background:linear-gradient(135deg,#2c3540,#8fa3b5 50%,#2f7fd0)"></div>
    <h3>fitness Consultation</h3>
    <p>Lorem Ipsum is simply dummy text of the printing and typesetting industry.</p>
    <div class="btn btn-orange">Read More</div>
  </article>
  <article class="abs card" style="left:425px">
    <div class="photo" role="img" aria-label="Man meditating outdoors among green trees" style="background:linear-gradient(135deg,#4d6b2a,#a9c46a 45%,#3b6fc8 80%)"></div>
    <h3>stress management</h3>
    <p>Lorem Ipsum is simply dummy text of the printing and typesetting industry.</p>
    <div class="btn btn-orange">Read More</div>
  </article>
  <article class="abs card" style="left:790px">
    <div class="photo" role="img" aria-label="Woman stretching her arms by a lake at sunrise" style="background:linear-gradient(180deg,#dfe6e8,#b7c4c6 50%,#8b8470)"></div>
    <h3>holistic health</h3>
    <p>Lorem Ipsum is simply dummy text of the printing and typesetting industry.</p>
    <div class="btn btn-orange">Read More</div>
  </article>
</section>

<section class="about">
  <h2 class="abs">About Tovan Health<br>Services</h2>
  <h4 style="top:219px">Our Mission</h4>
  <p style="top:251px;width:455px">At Tovan Health Services, we are committed to providing top-notch health consulting services to our clients. Our mission is to help people achieve optimal health and wellness through personalized plans and ongoing support.</p>
  <h4 style="top:347px">Our Team</h4>
  <p style="top:379px;width:400px">Our team of experienced health consultants has a diverse range of expertise, from nutrition and fitness to stress management and holistic health. We work together to develop customized solutions for each client, based on their unique needs and goals.</p>
  <div class="photo about-big" role="img" aria-label="Woman with arms open enjoying sunlight outdoors"></div>
  <div class="photo about-small" role="img" aria-label="Woman in profile at golden hour"></div>
</section>

<section class="testimonials">
  <div class="photo" role="img" aria-label="Client portrait in an office" style="left:188px;top:56px;width:169px;height:168px;background:linear-gradient(135deg,#e7e9ec,#8b2a2e 60%,#c9ccd0)"></div>
  <div class="photo" role="img" aria-label="Client portrait outdoors" style="left:842px;top:56px;width:169px;height:168px;border-radius:0 40px 0 0;background:linear-gradient(135deg,#8ea77a,#d9b89a 50%,#e8e8e2)"></div>
  <div class="photo" role="img" aria-label="Client portrait in a garden" style="left:322px;top:304px;width:113px;height:111px;border-radius:0 0 0 30px;background:linear-gradient(135deg,#7a9a52,#c48a6e 55%,#e98a8a)"></div>
  <div class="photo" role="img" aria-label="Client portrait outdoors" style="left:764px;top:304px;width:112px;height:111px;border-radius:0 0 30px 0;background:linear-gradient(135deg,#a8b48a,#5a3a2a 55%,#c9c8b8)"></div>
  <h2 class="abs">Customer<br>Testimonials</h2>
  <div class="abs stars">
    <svg width="20" height="20" viewBox="0 0 20 20"><path fill="#f6b91a" d="M10 1l2.7 5.8 6.3.7-4.7 4.3 1.3 6.2L10 14.9 4.4 18l1.3-6.2L1 7.5l6.3-.7z"/></svg>
    <svg width="20" height="20" viewBox="0 0 20 20"><path fill="#f6b91a" d="M10 1l2.7 5.8 6.3.7-4.7 4.3 1.3 6.2L10 14.9 4.4 18l1.3-6.2L1 7.5l6.3-.7z"/></svg>
    <svg width="20" height="20" viewBox="0 0 20 20"><path fill="#f6b91a" d="M10 1l2.7 5.8 6.3.7-4.7 4.3 1.3 6.2L10 14.9 4.4 18l1.3-6.2L1 7.5l6.3-.7z"/></svg>
    <svg width="20" height="20" viewBox="0 0 20 20"><path fill="#f6b91a" d="M10 1l2.7 5.8 6.3.7-4.7 4.3 1.3 6.2L10 14.9 4.4 18l1.3-6.2L1 7.5l6.3-.7z"/></svg>
    <svg width="20" height="20" viewBox="0 0 20 20"><path fill="#f6b91a" d="M10 1l2.7 5.8 6.3.7-4.7 4.3 1.3 6.2L10 14.9 4.4 18l1.3-6.2L1 7.5l6.3-.7z"/></svg>
  </div>
  <p class="abs quote">Lorem Ipsum is simply dummy text of the printing and typesetting industry. Sed ut perspiciatis unde omnis iste natus error sit voluptatem lorem ipsum dolor</p>
  <div class="abs client"><div class="avatar" role="img" aria-label="Client avatar"></div>Client</div>
</section>

<section class="who">
  <div class="abs who-frame-top"></div>
  <div class="abs who-frame-bot"></div>
  <div class="photo who-photo" role="img" aria-label="Smiling nurse embracing an older woman"></div>
  <h2 class="abs">who we are?</h2>
  <p>Lorem Ipsum has been the industry's standard dummy text ever since the 1500s, when an unknown printer took a galley of type and scrambled it to make a type specimen book. It has survived not only five centuries, but also the leap into electronic typesetting, remaining essentially unchanged.</p>
  <div class="btn btn-orange">Learn More</div>
</section>

<section class="booking">
  <h2 class="abs section-title">Book an Appointment</h2>
  <div class="field filled" style="top:150px">Full Name *</div>
  <div class="field" style="top:205px">Eamil *</div>
  <div class="field" style="top:261px">Phone Number *</div>
  <div class="field notes" style="top:317px">Other Notes *</div>
  <div class="btn btn-orange">Submit</div>
</section>

<footer class="site-footer">
  <h5 style="left:60px">contact</h5>
  <div class="contact-row" style="top:87px">
    <span class="icon-ring"><svg width="16" height="16" viewBox="0 0 24 24"><path fill="none" stroke="#0e1d3f" stroke-width="2" d="M5 3h4l2 5-2.5 1.5a11 11 0 0 0 6 6L16 13l5 2v4a2 2 0 0 1-2 2A17 17 0 0 1 3 5a2 2 0 0 1 2-2z"/></svg></span>+ 202-555-0147
  </div>
  <div class="contact-row" style="top:134px">
    <span class="icon-ring"><svg width="16" height="16" viewBox="0 0 24 24"><rect x="4" y="8" width="16" height="12" rx="2" fill="none" stroke="#0e1d3f" stroke-width="2"/><rect x="7" y="3" width="10" height="6" fill="none" stroke="#0e1d3f" stroke-width="2"/></svg></span>+ 202-555-0183
  </div>
  <div class="contact-row" style="top:181px">
    <span class="icon-ring"><svg width="16" height="16" viewBox="0 0 24 24"><rect x="3" y="6" width="18" height="12" rx="1" fill="none" stroke="#0e1d3f" stroke-width="2"/><path d="M3 6l9 7 9-7" fill="none" stroke="#0e1d3f" stroke-width="2"/></svg></span>info@tovanhealthservices.com
  </div>
  <div class="contact-row" style="top:228px">
    <span class="icon-ring"><svg width="16" height="16" viewBox="0 0 24 24"><path d="M12 22s7-7 7-12a7 7 0 0 0-14 0c0 5 7 12 7 12z" fill="none" stroke="#0e1d3f" stroke-width="2"/><circle cx="12" cy="10" r="2.5" fill="#0e1d3f"/></svg></span>4180 Larkspur Avenue NW, Suite 210<br>Washington, DC 20417
  </div>

  <h5 style="left:426px">Hours</h5>
  <div class="hours">
    <div><b>Mon</b> 09:00 am – 05:00 pm</div>
    <div><b>Tue</b> 09:00 am – 05:00 pm</div>
    <div><b>Wed</b> 09:00 am – 05:00 pm</div>
    <div><b>Thu</b> 09:00 am – 05:00 pm</div>
    <div><b>Fri</b> 09:00 am – 05:00 pm</div>
    <div><b>Sat</b> 10:00 am – 02:00 pm</div>
    <div><b>Sun</b> Closed</div>
  </div>

  <div class="news">
    <h5 style="left:791px">Join Our Mailing List</h5>
    <p>Get 10% off your first purchase when you sign up for our newsletter!</p>
    <div class="field">Email *</div>
  </div>
  <div class="btn btn-orange">Submit</div>

  <div class="abs copy-line"></div>
  <div class="abs copy">Copyright © 2025 Tovan Health Services - All Rights Reserved.</div>
</footer>

</body>
</html>
```